Finally a Vodka produced for women ! (Label Design)

We are a small distillery based in Melbourne, Australia and we need a Vodka label design solution that will appeal to women aged 30-50 years and radiate luxury. Full Details are in a design brief attached. We thank you in advance.

Target Market(s)

Affluent females 30-50 years.

Industry/Entity Type

Spirits/Alcohol

Requirements
Must have
• Be clear this is a luxury Vodka.
Nice to have
• Elegance.

```html
<!DOCTYPE html>
<html lang="en">
<head>
<meta charset="utf-8">
<title>Ivory Larke Handcrafted Vodka – Label</title>
<link rel="stylesheet" href="https://fonts.googleapis.com/css2?family=Montserrat:wght@500&family=Pinyon+Script&family=Tinos:ital,wght@0,400;1,400&display=swap">
<style>
  :root {
    --canvas: #ffffff;
    --ink: #4a4a4a;
    --cap-pink: #f4c6ef;
    --silver-light: #f2f2f2;
    --silver-mid: #c4c4c4;
    --silver-dark: #8e8e8e;
    --script-silver: #a9a9ab;
    --quartz-light: #f6d7f0;
    --quartz-mid: #ea9fdd;
    --quartz-deep: #d57cc6;
    --label-ink: #111111;
  }
  * { margin: 0; padding: 0; box-sizing: border-box; }
  html, body { width: 1200px; height: 900px; overflow: hidden; background: var(--canvas); }
  .artboard { position: relative; width: 1200px; height: 900px; }

  .cap-seal {
    position: absolute; left: 550px; top: 40px;
    width: 100px; height: 100px; border-radius: 50%;
    background: var(--cap-pink);
  }
  .cap-seal::after {
    content: ""; position: absolute; inset: 10px; border-radius: 50%;
    border: 3px solid var(--silver-mid);
  }

  .brand-name {
    position: absolute; left: 0; top: 200px; width: 1200px;
    text-align: center;
    font-family: "Montserrat", sans-serif; font-weight: 500;
    font-size: 50px; line-height: 64px; letter-spacing: 12px;
    padding-left: 12px;
    color: var(--ink);
  }

  .front-label { position: absolute; left: 370px; top: 360px; width: 460px; height: 476px; }
  .front-label svg { display: block; width: 100%; height: 100%; }

  .label-copy {
    position: absolute; left: 370px; top: 360px; width: 460px; height: 476px;
    text-align: center; color: var(--label-ink);
  }
  .label-copy .handcrafted {
    position: absolute; top: 50px; width: 100%;
    font-family: "Tinos", serif; font-style: italic;
    font-size: 24px; letter-spacing: 3px;
  }
  .label-copy .spirit-type {
    position: absolute; top: 62px; width: 100%;
    font-family: "Pinyon Script", cursive;
    font-size: 120px; line-height: 150px;
    color: var(--script-silver);
  }
  .label-copy .filtered {
    position: absolute; top: 200px; width: 100%;
    font-family: "Tinos", serif; font-style: italic; font-size: 20px;
  }
  .label-copy .origin {
    position: absolute; top: 226px; width: 100%;
    font-family: "Tinos", serif; font-size: 35px;
  }
  .label-copy .strength {
    position: absolute; top: 338px; width: 100%;
    font-family: "Tinos", serif; font-size: 24px;
  }
  .label-copy .strength small { font-size: 12px; }
  .label-copy .rule {
    position: absolute; top: 372px; left: 170px; width: 120px;
    border-top: 2px solid var(--label-ink);
  }
  .label-copy .volume {
    position: absolute; top: 378px; width: 100%;
    font-family: "Tinos", serif; font-size: 24px;
  }
  .label-copy .volume small { font-size: 12px; }
</style>
</head>
<body>
<main class="artboard">
  <div class="cap-seal"></div>

  <h1 class="brand-name">IVORY<br>LARKE</h1>

  <div class="front-label">
    <svg viewBox="0 0 290 300" role="img" aria-label="Rose quartz stone texture on the label panel, framed in silver foil">
      <defs>
        <linearGradient id="silver-frame" x1="0" y1="0" x2="1" y2="1">
          <stop offset="0" stop-color="var(--silver-light)"/>
          <stop offset="0.35" stop-color="var(--silver-dark)"/>
          <stop offset="0.6" stop-color="var(--silver-light)"/>
          <stop offset="1" stop-color="var(--silver-mid)"/>
        </linearGradient>
        <linearGradient id="quartz-fill" x1="0" y1="0" x2="1" y2="1">
          <stop offset="0" stop-color="var(--quartz-mid)"/>
          <stop offset="0.3" stop-color="var(--quartz-light)"/>
          <stop offset="0.55" stop-color="var(--quartz-mid)"/>
          <stop offset="0.8" stop-color="var(--quartz-light)"/>
          <stop offset="1" stop-color="var(--quartz-deep)"/>
        </linearGradient>
      </defs>
      <path d="M45 6 L245 6 L284 75 L205 294 L85 294 L6 75 Z"
            fill="url(#quartz-fill)" stroke="url(#silver-frame)" stroke-width="10" stroke-linejoin="round"/>
      <path d="M49 13 L241 13 L276 75 L200 287 L90 287 L14 75 Z"
            fill="none" stroke="var(--silver-light)" stroke-width="1" stroke-linejoin="round" opacity="0.8"/>
    </svg>
  </div>

  <div class="label-copy">
    <p class="handcrafted">Handcrafted</p>
    <p class="spirit-type">Vodka</p>
    <p class="filtered">filtered with natural</p>
    <p class="origin">Australian Rose Quartz</p>
    <p class="strength">40% <small>ALC/VOL</small></p>
    <span class="rule"></span>
    <p class="volume">700<small>ml</small></p>
  </div>
</main>
</body>
</html>
```